Tarjetas de visita para empresa de aluminio

Empresa con mas de 40 años vendiendo perfiles de aluminio.
Somos fábrica y almacén, queremos renovar la tarjeta de presentación de nuestros comerciales dando una imgen innovadora y tecnógica mezclado con la calidez del respeto al medio ambiente.
Añado el logo de la empresa y actual cara trasera de la tarjeta de visita, el logo es el simbolo WM y la marca TRAVENIC EXTRUSION, la frase 2extrusion y lacado de aluminio" debe cambiarse por "Diseño, extrusión, lacado, anodizado y mecanizado de precisión de aluminio" o en su defecto incluir todos esos servicios que hacemos o una frase mas pegadiza.

We are an aluminium factory, we produce and stock profiles of aluminium.
we want to renew visit card of our sellers, we are looking for something that show innovation, tecnology and environment respect.
Upload our actual logo and back of visit card, logo WM and brand TRAVENIC EXTRUSION must be keept.
Text "Extrusion y lacado de aluminio" must be changed for "Diseño, extrusion, lacado, anodizado y mecanizado de precisión de aluminio" or something like that

```html
<!DOCTYPE html>
<html lang="es">
<head>
<meta charset="utf-8">
<title>Tarjetas de visita – Travenic Extrusion</title>
<link rel="stylesheet" href="https://fonts.googleapis.com/css2?family=Arimo:wght@400&family=Teko:wght@400;500&display=swap">
<style>
  :root {
    --navy: #1f3169;
    --accent: #2f63b8;
    --ink: #1a1a1a;
    --paper: #ffffff;
    --backdrop: #e4e5e7;
    --silver: #e9ecf2;
  }
  * { margin: 0; padding: 0; box-sizing: border-box; }
  html, body { width: 1200px; height: 1200px; overflow: hidden; }
  body { background: var(--backdrop); position: relative; font-family: "Arimo", Arial, sans-serif; }

  .card {
    position: absolute; top: 389px; width: 240px; height: 420px;
    border-radius: 19px; overflow: hidden;
  }
  .card-front { left: 335px; background: var(--paper); }
  .card-back { left: 623px; background: var(--navy); }

  .brand-seal {
    position: absolute; width: 62px; height: 62px; border-radius: 50%;
    left: 50%; transform: translateX(-50%);
  }
  .card-front .brand-seal { top: 20px; border: 3px solid var(--navy); }
  .card-back .brand-seal { top: 301px; border: 3px solid var(--silver); }

  .brand-name {
    position: absolute; left: 0; right: 0; text-align: center;
    font-family: "Teko", "Arial Narrow", sans-serif; font-weight: 500;
    font-size: 23px; letter-spacing: 1.5px; line-height: 1;
  }
  .card-front .brand-name { top: 90px; color: var(--navy); }
  .card-back .brand-name { top: 368px; color: var(--silver); }

  .brand-tick { position: absolute; top: 91px; width: 4px; height: 18px; background: var(--accent); }
  .brand-tick.left { left: 0; }
  .brand-tick.right { right: 0; }

  .holder-name {
    position: absolute; left: 16px; top: 177px;
    font-family: "Teko", "Arial Narrow", sans-serif; font-weight: 500;
    font-size: 20px; letter-spacing: 1.6px; color: var(--navy); line-height: 1;
  }
  .holder-role { position: absolute; left: 16px; top: 197px; font-size: 12px; color: var(--ink); }

  .contact-list { position: absolute; left: 16px; top: 228px; list-style: none; }
  .contact-list li {
    display: flex; align-items: center; height: 13.7px;
    font-size: 12px; color: var(--ink); line-height: 1;
  }
  .contact-list svg { width: 9px; height: 9px; margin-right: 7px; flex: none; fill: var(--accent); }
  .contact-list .highlight { color: var(--accent); }

  .divider { position: absolute; left: 16px; top: 310px; width: 145px; height: 1px; background: var(--navy); }

  .address { position: absolute; left: 16px; top: 323px; font-size: 12px; line-height: 13.7px; color: var(--ink); }
  .address .street { color: var(--accent); }

  .service-band {
    position: absolute; left: 0; right: 0; bottom: 0; height: 35px;
    background: var(--navy); display: flex; align-items: center; justify-content: center;
  }
  .service-line {
    font-family: "Teko", "Arial Narrow", sans-serif; font-weight: 400;
    font-size: 9px; letter-spacing: 0.1px; color: var(--paper); text-transform: uppercase; padding-top: 2px;
  }

  .back-strip { position: absolute; left: 18px; width: 204px; bottom: 0; height: 6px; background: var(--accent); }
</style>
</head>
<body>

<section class="card card-front">
  <div class="brand-seal"></div>
  <span class="brand-tick left"></span>
  <div class="brand-name">TRAVENIC EXTRUSION</div>
  <span class="brand-tick right"></span>

  <div class="holder-name">ÁLVARO MORENO RUIZ</div>
  <div class="holder-role">Comercial</div>

  <ul class="contact-list">
    <li><svg viewBox="0 0 10 10"><path d="M2.5 0h5a1 1 0 0 1 1 1v8a1 1 0 0 1-1 1h-5a1 1 0 0 1-1-1V1a1 1 0 0 1 1-1zm.4 1.2v6.6h4.2V1.2zM5 8.3a.5.5 0 1 0 0 1 .5.5 0 0 0 0-1z"/></svg>600 41 27 85</li>
    <li><svg viewBox="0 0 10 10"><path d="M2.2.5l1.6 2-1 1a6 6 0 0 0 3.7 3.7l1-1 2 1.6-1 1.7C4.9 9.4.6 5.1.5 1.5z"/></svg>955 20 14 37</li>
    <li><svg viewBox="0 0 10 10"><path d="M2.5 0h5v3h-5zM.5 3.5h9v4h-2V10h-5V7.5h-2zm3 4v1.5h3V7.5z"/></svg>955 20 14 90</li>
    <li><svg viewBox="0 0 10 10"><path d="M0 2h10v6.5H0zm1 .8L5 5.6 9 2.8v-.1H1zM1 3.9v3.8h8V3.9L5 6.7z"/></svg>alvaromoreno@travenic.com</li>
    <li><svg viewBox="0 0 10 10"><path d="M5 0a5 5 0 1 0 0 10A5 5 0 0 0 5 0zm-.5 1.1v1.7H2.9a4 4 0 0 1 1.6-1.7zm1 0a4 4 0 0 1 1.6 1.7H5.5zM1.2 3.8h3.3v1.7H1.1zm4.3 0h3.3l.1 1.7H5.5zM1.3 6.5h3.2v2.4a4 4 0 0 1-3.2-2.4zm4.2 0h3.2a4 4 0 0 1-3.2 2.4z"/></svg>www.<span class="highlight">travenic</span>.com</li>
  </ul>

  <div class="divider"></div>

  <address class="address" style="font-style:normal">
    <div class="street">Pol. Ind. Norte - C/ 4 N° 12</div>
    <div>41900 VILLANUEVA DEL RÍO (Sevilla)</div>
    <div>Apartado de Correos 245</div>
  </address>

  <div class="service-band">
    <p class="service-line">Diseño, extrusion, lacado, anodizado y mecanizado de precisión de aluminio</p>
  </div>
</section>

<section class="card card-back">
  <div class="brand-seal"></div>
  <div class="brand-name">TRAVENIC EXTRUSION</div>
  <span class="back-strip"></span>
</section>

</body>
</html>
```